New Business Cards for Organic Meat Farm

We need a business card designed for Thornedge Farm, a meat farm in western MA. Our logo uses a hand-drawn woodcut (attached). Our color palette has been simply black and white (shown in notepad and picture of our food truck). While we are based out of western MA, we have ambitions to grow nationally, so our hope is for a classy and memorable card which will be printed on a premium quality stock from a printer like plavix.com.
Target Market(s)
consumers of quality meats, restauranteurs, partnering farms
Industry/Entity Type
Farming and prepared meat products
Contact Information for Business Card
Wendel Ruark, President/Owner, wendel@thornedgefarm.example, mobile: 555-014-2761, phone: 555-019-6083, thornedgefarm.example, facebook: @thornedgefarm, instagram: @thornedgefarmne
Colors
Designer to choose colors to be used in the design.
Look and feel

```html
<!DOCTYPE html>
<html lang="en">
<head>
<meta charset="utf-8">
<title>Thornedge Farm — Business Card</title>
<link href="https://fonts.googleapis.com/css2?family=Libre+Baskerville:wght@400;700&family=Poppins:wght@300;400&display=swap" rel="stylesheet">
<style>
  :root {
    --ink: #0d0d0d;
    --paper: #ffffff;
    --backdrop: #9e9e9e;
    --woodcut-dark: #2a2a2a;
    --woodcut-light: #8a8a8a;
  }
  * { box-sizing: border-box; margin: 0; padding: 0; }
  html, body {
    width: 1092px; height: 1200px; overflow: hidden;
    background: var(--backdrop);
  }
  .sheet {
    width: 1092px; height: 1200px;
    display: flex; flex-direction: column; align-items: center; justify-content: center;
    gap: 40px;
  }
  .card {
    position: relative;
    width: 880px; height: 498px;
    background: var(--paper);
    overflow: hidden;
    box-shadow: 0 2px 6px rgba(0,0,0,.15);
  }
  .card-shapes { position: absolute; inset: 0; width: 100%; height: 100%; }

  /* Front */
  .woodcut-front {
    position: absolute; left: 274px; top: 38px; width: 332px; height: 208px;
    border-radius: 50% 50% 6px 6px / 70% 70% 6px 6px;
    background: linear-gradient(180deg, var(--woodcut-dark) 0%, var(--woodcut-light) 55%, var(--woodcut-dark) 100%);
  }
  .brand-name {
    position: absolute; left: 0; right: 0; top: 268px;
    text-align: center;
    font-family: "Libre Baskerville", serif; font-weight: 700;
    font-size: 52px; color: var(--ink); letter-spacing: .5px;
  }

  /* Back */
  .woodcut-back {
    position: absolute; left: 56px; top: 28px; width: 200px; height: 116px;
    border-radius: 50% 50% 4px 4px / 70% 70% 4px 4px;
    background: linear-gradient(180deg, var(--woodcut-dark) 0%, var(--woodcut-light) 55%, var(--woodcut-dark) 100%);
  }
  .contact {
    position: absolute; right: 30px; top: 44px; width: 380px;
    color: var(--paper); text-align: right;
  }
  .contact-name {
    font-family: "Libre Baskerville", serif; font-size: 30px; letter-spacing: 1px;
    margin-right: 24px;
  }
  .contact-title {
    font-family: "Poppins", sans-serif; font-weight: 300; font-size: 19px;
    margin-right: 24px; margin-top: 2px;
  }
  .contact-group { margin-top: 50px; }
  .contact-group + .contact-group { margin-top: 40px; }
  .contact-line {
    display: flex; justify-content: flex-end; align-items: center; gap: 12px;
    font-family: "Poppins", sans-serif; font-weight: 300; font-size: 18px; line-height: 31px;
  }
  .contact-icon { width: 12px; height: 12px; flex: none; }
  .contact-icon.blank { visibility: hidden; }
</style>
</head>
<body>
<main class="sheet">

  <section class="card card-front">
    <div class="woodcut-front" role="img" aria-label="Woodcut illustration of the farmhouse with porch and trees"></div>
    <h1 class="brand-name">Thornedge Farm</h1>
    <svg class="card-shapes" viewBox="0 0 880 498" aria-hidden="true">
      <rect x="0" y="472" width="880" height="14" fill="var(--ink)"/>
      <rect x="0" y="492" width="880" height="3" fill="var(--ink)"/>
    </svg>
  </section>

  <section class="card card-back">
    <div class="woodcut-back" role="img" aria-label="Small woodcut illustration of the farmhouse"></div>
    <svg class="card-shapes" viewBox="0 0 880 498" aria-hidden="true">
      <polygon points="553,0 880,0 880,498 315,498" fill="var(--ink)"/>
      <polygon points="538,0 546,0 308,498 300,498" fill="var(--ink)"/>
      <rect x="0" y="476" width="250" height="12" fill="var(--ink)"/>
      <polygon points="258,476 268,476 262,488 252,488" fill="var(--ink)"/>
      <polygon points="274,476 284,476 278,488 268,488" fill="var(--ink)"/>
    </svg>
    <div class="contact">
      <h2 class="contact-name">WENDEL RUARK</h2>
      <p class="contact-title">President/Owner</p>
      <div class="contact-group">
        <p class="contact-line">555-014-2761
          <svg class="contact-icon" viewBox="0 0 12 12"><circle cx="6" cy="6" r="6" fill="#fff"/><path d="M3.3 6.2 5.2 8 8.8 4" stroke="#0d0d0d" stroke-width="1.4" fill="none"/></svg></p>
        <p class="contact-line">555-019-6083<svg class="contact-icon blank" viewBox="0 0 12 12"></svg></p>
      </div>
      <div class="contact-group">
        <p class="contact-line">wendel@thornedgefarm.example
          <svg class="contact-icon" viewBox="0 0 12 12"><circle cx="6" cy="6" r="5" fill="none" stroke="#fff" stroke-width="2"/></svg></p>
        <p class="contact-line">thornedgefarm.example
          <svg class="contact-icon" viewBox="0 0 12 12"><circle cx="6" cy="6" r="5" fill="none" stroke="#fff" stroke-width="2"/></svg></p>
      </div>
      <div class="contact-group">
        <p class="contact-line">@thornedgefarm
          <svg class="contact-icon" viewBox="0 0 12 12"><circle cx="6" cy="6" r="6" fill="#fff"/></svg></p>
        <p class="contact-line">@thornedgefarmne
          <svg class="contact-icon" viewBox="0 0 12 12"><circle cx="6" cy="6" r="6" fill="#fff"/></svg></p>
      </div>
    </div>
  </section>

</main>
</body>
</html>
```